Advertisement Design Project

PLEASE SEE DIMENSION REQUIREMENTS:
Ad size is: 3 3/8" x 9 1/2"
Full color
Output to PDF File (press optimized, CMYK, fonts embedded, 300 dpi).

I am looking for a full-color advertisement for a professional guide that is printed annually. I am a law firm servicing the LGBT community in the greater Seattle, Washington, USA area.

I have attached a mock-up idea similar to what I'd like, but I am open to different design elements and copy. The copy should at the very least list the broad legal practice areas I have mentioned.

The final deisgn should be simple, elegant, and convey that my law firm is the trusted choice for LGBT individuals, families and small businesses.

I've uploaded my logo and some of the original photo elements.

Thank you!

Reason: I've seen so many great designs that I need another day to follow-up with everyone. Thank you very much for your submissions!

Target Market(s)

LGBT individuals and families in need of legal services.

Industry/Entity Type

Law Firm

Requirements
Must have
• It must have our logo, web address, phone number, and email address.

```html
<!DOCTYPE html>
<html lang="en">
<head>
<meta charset="utf-8">
<title>Meridian Law PS – Advertisement</title>
<link rel="stylesheet" href="https://fonts.googleapis.com/css2?family=Arimo:wght@400;700&display=swap">
<style>
  :root {
    --page: #ffffff;
    --ink-dark: #141313;
    --ink-mid: #2a2522;
    --wood-dark: #4a2a16;
    --wood: #8a5228;
    --wood-light: #b8753c;
    --accent-red: #e8231f;
    --text-light: #ffffff;
    --text-soft: #e9e4df;
    --photo-sky: #8ea3ae;
    --photo-suit: #2c3140;
  }
  * { margin: 0; padding: 0; box-sizing: border-box; }
  html, body {
    width: 1200px; height: 2384px; overflow: hidden;
    background: var(--page);
    font-family: "Arimo", Arial, sans-serif;
  }
  .ad {
    position: absolute; left: 214px; top: 104px;
    width: 780px; height: 2190px;
    overflow: hidden;
    color: var(--text-light);
  }
  .ad-backdrop {
    position: absolute; inset: 0;
    background: linear-gradient(180deg,
      var(--ink-dark) 0%, var(--ink-dark) 42%,
      var(--ink-mid) 58%, var(--wood-dark) 78%,
      var(--wood) 92%, var(--wood-light) 100%);
  }
  .brand-mark {
    position: absolute; left: 300px; top: 150px;
    width: 180px; height: 180px;
    border-radius: 50%;
    border: 14px solid var(--accent-red);
  }
  .brand-name {
    position: absolute; left: 0; right: 0; top: 400px;
    text-align: center;
    font-weight: 400; font-size: 104px; letter-spacing: -2px;
    color: var(--accent-red);
  }
  .intro {
    position: absolute; left: 46px; width: 694px; top: 584px;
    font-weight: 700; font-size: 34px; line-height: 56px;
    text-align: justify; text-align-last: left;
    letter-spacing: 0.5px;
  }
  .portrait {
    position: absolute; left: 626px; top: 790px;
    width: 720px; height: 720px; border-radius: 50%;
    border: 16px solid var(--accent-red);
    background: radial-gradient(circle at 40% 55%, var(--photo-suit) 0%, var(--photo-suit) 30%, #5c6670 55%, var(--photo-sky) 100%);
  }
  .practice-list {
    position: absolute; left: 46px; top: 948px;
    list-style: none;
    font-weight: 700; font-size: 42px; line-height: 50px;
  }
  .practice-list li { margin-bottom: 64px; }
  .practice-list li.last { margin-bottom: 0; }
  .practice-list .indent { display: block; padding-left: 28px; }
  .call-to-action {
    position: absolute; left: 20px; width: 740px; top: 1630px;
    text-align: center;
    font-weight: 700; font-size: 34px; line-height: 54px;
  }
  .attorney {
    position: absolute; left: 470px; width: 300px; top: 2010px;
    text-align: center;
    font-weight: 400; font-size: 30px; line-height: 42px;
    color: var(--text-soft);
  }
  .contact-web {
    position: absolute; left: 0; right: 0; top: 2128px;
    text-align: center;
    font-weight: 700; font-size: 38px;
  }
  .contact-address {
    position: absolute; left: 0; right: 0; top: 2198px;
    text-align: center;
    font-weight: 700; font-size: 30px;
  }
</style>
</head>
<body>
  <section class="ad">
    <div class="ad-backdrop" role="img" aria-label="Dark law office scene with scales of justice and a wooden gavel on a desk"></div>

    <div class="brand-mark"></div>
    <div class="brand-name">Meridian Law PS</div>

    <p class="intro">Proudly serves as the trusted legal advisor to hundreds of LGBT individuals and families for their:</p>

    <div class="portrait" role="img" aria-label="Portrait of the attorney in a suit seated at a desk before a city window"></div>

    <ul class="practice-list">
      <li>- estate planning,</li>
      <li>- probate,</li>
      <li>- real estate, &amp;</li>
      <li class="last">- small business<span class="indent">needs.</span></li>
    </ul>

    <p class="call-to-action">Contact Meridian Law PS so that you too can discover unparalleled service and value in the delivery of legal services. Because you should trust your attorney.</p>

    <p class="attorney">Daniel R. Whitford<br>Attorney &amp; Principal</p>

    <p class="contact-web">www.meridian-law.com | (206) 555-0148</p>
    <p class="contact-address">1450 Harbor Ave #300 | Seattle, WA 98101</p>
  </section>
</body>
</html>
```